Health software company called BRIGHT HARBOR, committed to innovation and technological excellence

The powerpoint presentation template is necessary, very necessary is elegant and modern with innovative images and the color palette attached. The presentation will be used for the business plan and investor presentations that we will use to raise funds. Please, recommend a modern typeface, as well as format to be able to use it and incorporate it as part of the company's brand guidelines. Great diversity of technological solutions

Very low attendance of designers for a high budget. Very few proposals and no capture my interest

Target Market(s)

managers, managers of public and private health centers, government states, investors

Industry/Entity Type

It Company

Font styles to use
Serif

Requirements
Must have
• The powerpoint presentation template is necessary, very necessary is elegant, minimalist and modern with innovative images and the color palette attached. it must be refined in demarcated style
Nice to have
• very nice, visually harmonic avoid saturation
Should not have
• NO dark colors NO dark colors NO dark colors NO dark colors NO dark colors

```html
<!DOCTYPE html>
<html lang="en">
<head>
<meta charset="utf-8">
<title>Bright Harbor – Presentation Template</title>
<link href="https://fonts.googleapis.com/css2?family=Oswald:wght@400;500&family=Open+Sans:wght@300;400&family=Arimo:wght@400;700&display=swap" rel="stylesheet">
<style>
:root{
  --cyan:#1ab7ea;
  --ink:#111;
  --text:#222;
  --grey:#b3b3b3;
  --rule:#9a9a9a;
  --photo-a:#cfd8d4;
  --photo-b:#e9eef0;
  --s1:#a7a7a7;--s2:#6ccaf0;--s3:#bfdd93;--s4:#f9bd80;--s5:#bd88c9;--s6:#f393c6;
}
*{margin:0;padding:0;box-sizing:border-box}
html,body{width:1200px;height:761px;overflow:hidden;background:#fff}
body{position:relative;font-family:Arimo,Arial,sans-serif;color:var(--text)}
.slide{position:absolute;width:568px;height:320px;background:#fff;overflow:hidden;box-shadow:0 0 4px rgba(0,0,0,.25)}
.caption{position:absolute;width:568px;text-align:center;font-family:"Open Sans",sans-serif;font-weight:300;font-size:16px;color:#333}
.abs{position:absolute}
.logo-box{position:absolute;border:1px solid var(--ink);font-family:Oswald,sans-serif;font-weight:500;color:var(--ink);display:flex;align-items:center;justify-content:center;white-space:nowrap}
.site{position:absolute;font-size:6px;color:#333;display:flex;align-items:center;gap:4px}
.site .line{height:1px;background:var(--rule)}
.cover-title{position:absolute;left:17px;top:128px;font-family:Oswald,sans-serif;font-weight:500;line-height:1;letter-spacing:.5px}
.cover-title .a{color:var(--cyan);font-size:48px;display:block}
.cover-title .b{color:var(--ink);font-size:35px;display:block;margin-top:4px}
.band{position:absolute;left:0;top:114px;width:568px;height:91px;background:var(--cyan);color:#fff;text-align:center}
.band .kicker{position:absolute;top:6px;left:0;right:0;font-weight:700;font-size:10px}
.band .kicker span{border-bottom:1px solid #fff;padding-bottom:1px}
.band .quote{position:absolute;left:269px;top:28px;width:30px;height:30px;border:2px solid #fff;border-radius:50%;font-family:Oswald,sans-serif;font-size:24px;line-height:34px}
.band .headline{position:absolute;top:64px;left:0;right:0;font-family:Oswald,sans-serif;font-size:16.5px;letter-spacing:.2px}
.top-rule{position:absolute;left:51px;top:17px;right:0;height:1px;background:var(--ink)}
.section-tag{position:absolute;left:0;top:34px;height:16px;background:var(--cyan);color:#fff;font-weight:700;font-size:10.5px;line-height:16px;padding-left:17px}
.intro{position:absolute;left:17px;top:58px;width:536px;font-size:5.8px;line-height:10.5px;color:var(--ink)}
.tl-label{position:absolute;width:70px;text-align:center;font-size:3.8px;line-height:5px;color:var(--ink)}
.tl-label b{display:block;font-size:4.5px}
.step-tag{position:absolute;width:30px;text-align:center;font-size:3.5px;font-weight:700;color:var(--ink)}
.hist{position:absolute;width:140px;font-size:6px;line-height:10px;color:var(--ink)}
.hist b{display:block;color:var(--cyan);font-size:7px;line-height:9px}
.hist.left{text-align:right}
.pageno{position:absolute;left:546px;top:297px;font-size:5px;color:#333}
</style>
</head>
<body>

<!-- Cover -->
<section class="slide cover" style="left:20px;top:22px">
  <svg class="abs" width="568" height="320" viewBox="0 0 568 320" style="left:0;top:0">
    <defs>
      <linearGradient id="coverPhoto" x1="0" y1="0" x2="1" y2="1">
        <stop offset="0" stop-color="#5f7d52"/><stop offset=".55" stop-color="#c9d0c6"/><stop offset="1" stop-color="#eef0f0"/>
      </linearGradient>
    </defs>
    <polygon role="img" aria-label="Photo: smiling professional on the phone working at a laptop, plants behind" points="206,0 568,0 568,320 408,320" fill="url(#coverPhoto)"/>
    <polygon points="190,0 206,0 316,176 308,186" fill="var(--grey)"/>
    <polygon points="312,170 408,320 214,320" fill="var(--cyan)"/>
  </svg>
  <div class="logo-box" style="left:17px;top:18px;width:100px;height:34px;font-size:14px">BRIGHT HARBOR</div>
  <h1 class="cover-title"><span class="a">THINK AND</span><span class="b">DREAM DIGITAL</span></h1>
  <div class="site" style="left:17px;top:296px"><span>www.brightharbor-health.com</span><span class="line" style="width:178px"></span></div>
</section>
<div class="caption" style="left:20px;top:354px">COVER PAGE</div>

<!-- Back page -->
<section class="slide back" style="left:612px;top:22px">
  <div role="img" aria-label="Photo: hands writing with a pen beside a laptop keyboard on a white desk" class="abs" style="left:0;top:0;width:568px;height:320px;background:linear-gradient(135deg,#f4f6f8 0%,#dfe5ea 45%,#8c929a 75%,#e7ebee 100%)"></div>
  <div class="band">
    <div class="kicker"><span>WELCOME MESSAGE</span></div>
    <div class="quote">&ldquo;</div>
    <div class="headline">LOREM IPSUM IS SIMPLY DUMMY TEXT OF THE PRINTING AND TYPESETTING INDUSTRY</div>
  </div>
</section>
<div class="caption" style="left:612px;top:354px">BACK PAGE</div>

<!-- Page 01 -->
<section class="slide page-about" style="left:20px;top:392px">
  <div class="logo-box" style="left:16px;top:12px;width:32px;height:10px;font-size:4.5px;font-weight:400">BRIGHT HARBOR</div>
  <div class="top-rule"></div>
  <div class="section-tag" style="width:152px">ABOUT OUR COMPANY</div>
  <svg class="abs" width="24" height="22" style="left:143px;top:30px"><line x1="2" y1="1" x2="20" y2="20" stroke="var(--cyan)" stroke-width="1"/><line x1="6" y1="1" x2="24" y2="20" stroke="var(--cyan)" stroke-width="1"/></svg>
  <p class="intro">Lorem Ipsum is simply dummy text of the printing and typesetting industry. Lorem Ipsum has been the industry's standard dummy text ever since the 1500s, when an unknown printer took a galley of type and scrambled it to make a type specimen book. It has survived not only five centuries, but also the leap into electronic typesetting, remaining essentially unchanged. Lorem Ipsum is simply dummy text of the printing and typesetting industry. Lorem Ipsum has been the industry's standard dummy text ever since the 1500s.</p>
  <svg class="abs" width="568" height="320" viewBox="0 0 568 320" style="left:0;top:0">
    <rect x="50" y="179" width="93" height="7" fill="var(--s1)"/>
    <rect x="143" y="179" width="95" height="7" fill="var(--s2)"/>
    <rect x="238" y="179" width="92" height="7" fill="var(--s3)"/>
    <rect x="330" y="179" width="94" height="7" fill="var(--s4)"/>
    <rect x="424" y="179" width="94" height="7" fill="var(--s5)"/>
    <g stroke="#fff" stroke-width="2">
      <circle cx="50" cy="182" r="12" fill="var(--s1)"/>
      <circle cx="143" cy="182" r="12" fill="var(--s2)"/>
      <circle cx="238" cy="182" r="12" fill="var(--s3)"/>
      <circle cx="330" cy="182" r="12" fill="var(--s4)"/>
      <circle cx="424" cy="182" r="12" fill="var(--s5)"/>
      <circle cx="518" cy="182" r="12" fill="var(--s6)"/>
    </g>
    <g fill="none" stroke="#fff" stroke-width="1">
      <circle cx="50" cy="182" r="4"/>
      <rect x="138" y="178" width="10" height="7"/>
      <circle cx="238" cy="182" r="5"/>
      <rect x="325" y="178" width="10" height="8"/>
      <ellipse cx="424" cy="182" rx="6" ry="3"/><ellipse cx="424" cy="182" rx="3" ry="6"/>
      <circle cx="518" cy="182" r="5"/><line x1="513" y1="182" x2="523" y2="182"/>
    </g>
    <polygon points="46,197 54,197 50,202" fill="var(--s1)"/>
    <polygon points="139,167 147,167 143,162" fill="var(--s2)"/>
    <polygon points="234,197 242,197 238,202" fill="var(--s3)"/>
    <polygon points="326,167 334,167 330,162" fill="var(--s4)"/>
    <polygon points="420,197 428,197 424,202" fill="var(--s5)"/>
    <polygon points="514,167 522,167 518,162" fill="var(--s6)"/>
    <polygon points="568,248 568,320 496,320" fill="var(--cyan)"/>
  </svg>
  <div class="tl-label" style="left:15px;top:138px"><b>TITLE</b>Lorem ipsum is simply dummy text of the printing and typesetting industry.</div>
  <div class="step-tag" style="left:35px;top:206px">STEP 01</div>
  <div class="step-tag" style="left:128px;top:154px">STEP 02</div>
  <div class="tl-label" style="left:108px;top:200px"><b>TITLE</b>Lorem ipsum is simply dummy text of the printing and typesetting industry.</div>
  <div class="tl-label" style="left:203px;top:138px"><b>TITLE</b>Lorem ipsum is simply dummy text of the printing and typesetting industry.</div>
  <div class="step-tag" style="left:223px;top:206px">STEP 03</div>
  <div class="step-tag" style="left:315px;top:154px">STEP 04</div>
  <div class="tl-label" style="left:295px;top:200px"><b>TITLE</b>Lorem ipsum is simply dummy text of the printing and typesetting industry.</div>
  <div class="tl-label" style="left:389px;top:138px"><b>TITLE</b>Lorem ipsum is simply dummy text of the printing and typesetting industry.</div>
  <div class="step-tag" style="left:409px;top:206px">STEP 05</div>
  <div class="step-tag" style="left:503px;top:154px">STEP 06</div>
  <div class="tl-label" style="left:483px;top:200px"><b>TITLE</b>Lorem ipsum is simply dummy text of the printing and typesetting industry.</div>
  <div class="site" style="left:17px;top:297px"><span>www.brightharbor-health.com</span><span class="line" style="width:410px"></span></div>
  <div class="pageno" style="color:#fff">02</div>
</section>
<div class="caption" style="left:20px;top:730px">PAGE 01</div>

<!-- Page 02 -->
<section class="slide page-history" style="left:612px;top:392px">
  <div class="logo-box" style="left:16px;top:12px;width:32px;height:10px;font-size:4.5px;font-weight:400">BRIGHT HARBOR</div>
  <div class="top-rule"></div>
  <div class="section-tag" style="width:100px">OUR HISTORY</div>
  <svg class="abs" width="24" height="22" style="left:91px;top:30px"><line x1="2" y1="1" x2="20" y2="20" stroke="var(--cyan)" stroke-width="1"/><line x1="6" y1="1" x2="24" y2="20" stroke="var(--cyan)" stroke-width="1"/></svg>
  <svg class="abs" width="568" height="320" viewBox="0 0 568 320" style="left:0;top:0">
    <defs><radialGradient id="ring" cx=".5" cy=".5" r=".5"><stop offset=".7" stop-color="#f4f4f4"/><stop offset="1" stop-color="#e2e2e2"/></radialGradient></defs>
    <circle cx="275" cy="166" r="74" fill="url(#ring)"/>
    <circle cx="275" cy="166" r="57" fill="#fff"/>
    <circle cx="275" cy="166" r="54" fill="#ececec"/>
    <g fill="none" stroke="var(--ink)" stroke-width=".8">
      <polyline points="166,86 210,86 210,107 243,107"/>
      <line x1="170" y1="158" x2="212" y2="158"/>
      <polyline points="166,241 210,241 210,221 243,221"/>
      <polyline points="384,86 344,86 344,107 312,107"/>
      <line x1="384" y1="158" x2="340" y2="158"/>
      <polyline points="384,241 344,241 344,221 312,221"/>
    </g>
    <g fill="var(--ink)"><circle cx="166" cy="86" r="1.3"/><circle cx="170" cy="158" r="1.3"/><circle cx="166" cy="241" r="1.3"/><circle cx="384" cy="86" r="1.3"/><circle cx="384" cy="158" r="1.3"/><circle cx="384" cy="241" r="1.3"/></g>
    <polygon points="568,248 568,320 496,320" fill="var(--cyan)"/>
  </svg>
  <div class="logo-box" style="left:242px;top:155px;width:66px;height:22px;font-size:8px;background:#fff">BRIGHT HARBOR</div>
  <div class="hist left" style="left:24px;top:81px"><b>STEP 01</b>Lorem Ipsum is simply dummy text of the printing and typesetting.</div>
  <div class="hist left" style="left:24px;top:153px"><b>STEP 02</b>Lorem Ipsum is simply dummy text of the printing and typesetting industry.</div>
  <div class="hist left" style="left:24px;top:236px"><b>STEP 03</b>Lorem Ipsum is simply dummy text of the printing and typesetting.</div>
  <div class="hist" style="left:388px;top:81px"><b>STEP 04</b>Lorem Ipsum is simply dummy text of the printing and typesetting industry.</div>
  <div class="hist" style="left:388px;top:153px"><b>STEP 05</b>Lorem Ipsum is simply dummy text of the printing and typesetting industry.</div>
  <div class="hist" style="left:388px;top:236px"><b>STEP 06</b>Lorem Ipsum is simply dummy text of the printing and typesetting industry.</div>
  <div class="site" style="left:17px;top:297px"><span>www.brightharbor-health.com</span><span class="line" style="width:410px"></span></div>
  <div class="pageno" style="color:#fff">03</div>
</section>
<div class="caption" style="left:612px;top:730px">PAGE 02</div>

</body>
</html>
```